Trifold - Harbor Lantern Therapy

Maren Holloway, Psy.D.Licensed Psychologist

this is for hypnosis and meditation
I like decorative font for my name (conservative decorative)

calming effect is most imortant

Target Market(s)

clients with depression, pain, anxiety - adults and aged

Industry/Entity Type

Conservative

Font styles to use
Serif

Colors
abd037
85cae6
cadf82
34a7d7
ffffff
886aae
6b449b

Requirements
Must have
• I like zen-like calming effects. lime Green, light blues and purple. I like waves and color.
• I like water and light, flowers and plants - bamboo, stacking rocks, ocean, water, lotus flowers
Should not have
• not too much purple
• Mostly green and blue

```html
<!DOCTYPE html>
<html lang="en">
<head>
<meta charset="utf-8">
<title>Harbor Lantern Therapy – Trifold Inside</title>
<link href="https://fonts.googleapis.com/css2?family=Tenor+Sans&family=Lato:wght@400;700;900&family=Satisfy&display=swap" rel="stylesheet">
<style>
  :root {
    --aqua-top: #a9e3dc;
    --mint: #b6e6cf;
    --sage: #a9d9a8;
    --lime: #abd037;
    --sky: #85cae6;
    --purple: #6b449b;
    --lavender: #886aae;
    --ink: #1d1d24;
    --white: #ffffff;
    --backdrop: #3c3c3e;
  }
  * { box-sizing: border-box; margin: 0; padding: 0; }
  html, body {
    width: 1200px; height: 800px; overflow: hidden;
    background: var(--backdrop);
  }
  .trifold {
    position: absolute; left: 60px; top: 20px;
    width: 1080px; height: 760px;
    display: flex;
    background: linear-gradient(180deg, var(--aqua-top) 0%, var(--mint) 55%, var(--sage) 92%);
    border-bottom: 10px solid var(--purple);
    color: var(--ink);
    font-family: "Tenor Sans", sans-serif;
  }
  .panel {
    position: relative; width: 360px; height: 100%;
    padding: 40px 32px 20px 36px;
    border-right: 1px solid rgba(255,255,255,0.35);
    overflow: hidden;
  }
  .panel:last-child { border-right: none; }
  .panel > * { position: relative; }
  .panel--session { padding-top: 32px; }
  .dandelion-art {
    position: absolute; left: -40px; top: 400px;
    width: 300px; height: 300px; border-radius: 50%;
    background: radial-gradient(circle, rgba(255,255,235,0.85) 0%, rgba(230,240,190,0.55) 40%, rgba(200,225,170,0) 70%);
  }
  .seed-wash {
    position: absolute; inset: 0;
    background: radial-gradient(ellipse at 30% 40%, rgba(255,255,255,0.25), rgba(255,255,255,0) 60%);
  }
  .heading {
    font-size: 20px; font-weight: 400; line-height: 1.15; color: var(--ink);
  }
  .heading strong { color: var(--purple); font-family: "Lato", sans-serif; font-weight: 700; }
  .heading--caps { text-transform: uppercase; font-size: 18px; letter-spacing: 0.4px; }
  .heading--session { margin-top: 14px; font-size: 19px; }
  .rule { width: 52px; height: 2px; background: var(--ink); margin: 8px 0 11px; }
  .rule--tight { margin: 6px 0 8px; }
  .body-copy { font-size: 13px; line-height: 1.42; }
  .body-copy--small { font-size: 9.8px; line-height: 1.32; }
  .subhead {
    margin-top: 24px; font-family: "Lato", sans-serif; font-weight: 700;
    font-size: 21px; line-height: 1.1; color: var(--purple);
  }
  .ticks { list-style: none; margin-top: 4px; }
  .ticks li {
    position: relative; padding-left: 24px; margin-bottom: 5px;
    font-family: "Lato", sans-serif; font-weight: 900; font-size: 14px; line-height: 1.2;
  }
  .ticks li::before {
    content: ""; position: absolute; left: 4px; top: 2px;
    width: 5px; height: 10px;
    border-right: 2px solid var(--purple); border-bottom: 2px solid var(--purple);
    transform: rotate(40deg);
  }
  .ticks--light li { font-weight: 400; font-size: 11.5px; margin-bottom: 5px; }
  .mid-subhead {
    margin-top: 12px; font-family: "Lato", sans-serif; font-weight: 700;
    font-size: 13px; color: var(--purple);
  }
  .portrait-ring {
    width: 150px; height: 150px; border-radius: 50%;
    border: 8px solid var(--lime); margin: -10px 0 0 70px;
    background: radial-gradient(circle at 50% 40%, #f0dcc8 0%, #e8e6df 45%, #dfeef0 100%);
  }
  .doctor-name {
    margin: 12px 0 14px; font-family: "Satisfy", cursive;
    font-size: 30px; font-weight: 400; line-height: 1; color: var(--ink);
    white-space: nowrap;
  }
  .doctor-name sup { font-family: "Tenor Sans", sans-serif; font-size: 10px; vertical-align: 20px; }
  .bio p { font-size: 12.5px; line-height: 1.42; margin-bottom: 12px; }
</style>
</head>
<body>
<main class="trifold">
  <section class="panel panel--intro">
    <div class="dandelion-art" role="img" aria-label="Soft photograph of a dandelion seed head"></div>
    <h2 class="heading">What is <strong>Harbor Lantern Therapy (HLT)</strong></h2>
    <div class="rule"></div>
    <p class="body-copy">HLT dramatically enhances mood, creates calm, eases grief, optimizes health and promotes success. It is a form of hypnosis that clears stuck patterns of thinking and feeling at the subconscious level. Past emotionally charged memories are cleared. You do not have to talk about problems, share scattered thoughts, cry nor re-experience uncomfortable emotions. You are guided to engage in deep brain processing to create an internal shift for automatic changes in thoughts, feelings and behaviors. Profound change happens within your nervous system facilitating lasting positive effects. Only one or two sessions are needed to experience immediate symptom relief.</p>
    <h3 class="subhead">HLT is effective for many of life’s problems including:</h3>
    <div class="rule"></div>
    <ul class="ticks">
      <li>PTSD, Sexual Abuse and Childhood Abuse</li>
      <li>Grief, Infidelity and Heartbreak</li>
      <li>Relationship issues</li>
      <li>Anger and Resentment</li>
      <li>Guilt / Shame</li>
      <li>Anxiety / Fear</li>
      <li>Nightmares / Insomnia</li>
      <li>Stress-related symptoms and Pain</li>
    </ul>
  </section>

  <section class="panel panel--session">
    <div class="seed-wash" role="img" aria-label="Faint dandelion seeds drifting across the panel"></div>
    <h2 class="heading heading--caps">Clearing old stuff and making way for <strong>new beginnings</strong></h2>
    <div class="rule rule--tight"></div>
    <p class="body-copy body-copy--small">If you have been unable to change how you feel, think or act, it is likely that you are being affected by experiences from your past. When something is painful or disturbing, it slams into awareness and leaves a lasting impression. Even when the experience is finished, deeper parts of the mind may continue to respond as if the disturbing event is still occurring. When fueled by the ongoing influence of past events, emotional problems, destructive behaviors and relationship difficulties are impossible to overcome. You may consciously understand the value of changing a behavior, but unless your deeper mind is transformed, change is not likely. In HLT the subconscious mind is engaged, and the influence of past events is eliminated. Energy that was blocked is released and healing takes place. Negative habits and painful emotions are replaced by feelings of well-being and motivation for desired action.</p>
    <h2 class="heading heading--session">What happens in an <strong>HLT Session?</strong></h2>
    <div class="rule rule--tight"></div>
    <p class="body-copy body-copy--small">Trauma is stored in the mind and body. In HLT, you will experience profound physiological calm and you will be guided towards emotional resolution in a gentle, creative and even humorous way. You access inner resources of light, wisdom and peace. You step into the awareness of your wise and true self. As Elias Ward states: “we all have a beautiful light within, we just sometimes forget it is there.” From this place of light, emotional memories are easily reframed with new meaning. You will leave the session feeling peaceful and sourced from within by a free-flowing energy.</p>
    <h3 class="mid-subhead">Clear Your Mind and Change Your World</h3>
    <div class="rule rule--tight"></div>
    <ul class="ticks ticks--light">
      <li>Discover and resolve subconscious causes for emotional and behavioral difficulties</li>
      <li>Eliminate unconscious conflicts blocking desired change</li>
      <li>Promote mind / body healing</li>
    </ul>
  </section>

  <section class="panel panel--bio">
    <div class="portrait-ring" role="img" aria-label="Portrait photograph of Dr. Maren Holloway"></div>
    <h1 class="doctor-name">Dr. Maren Holloway <sup>Psy.D.</sup></h1>
    <div class="bio">
      <p>Dr. Holloway is a licensed clinical psychologist specializing in adults and seniors.</p>
      <p>She treats people for depression, anxiety, grief, sexual trauma, PTSD, relationship issues, infidelity, divorce and stress-related symptoms.</p>
      <p>She has over 20 years of clinical experience in mental health and is an adjunct counseling professor at Crestwood University.</p>
      <p>She received her Master’s and Doctorate degrees in Clinical Psychology from Alderbrook University in Bayport, Oregon.</p>
      <p>She earned a Bachelor’s of Science degree in Rehabilitation Medicine from Northvale University in Fairhaven, Canada. At Stillwater Wellness Center, she provides initial evaluations, assessment, diagnosis and comprehensive treatment planning.</p>
      <p>She will collaborate with you to create solutions for healing, empowerment and wellness.</p>
    </div>
  </section>
</main>
</body>
</html>
```